Professional PowerPoint Template for Data Reports, Presentations

We are a small leadership coaching/consulting firm and would like to update our PowerPoint template that we use with our clients, who are typically mid-senior level company professionals. I've attached a sample Powerpoint as well as our branding guide. The cover page is what needs the most work - just doesn't look current/professional enough. We do want to keep the pages after that clean, with come color but enough space for text and graphics.
Target Market(s)
Senior mgmt and HR executives in small-mid sized companies
Font styles to use
Sans Serif
Requirements
Must have
- Professional
- Clean
- Tied to company color scheme/logo
Nice to have
- Our title pages don't usually have many words on them; we'd like a design that has a lot of color - probably still using mainly our blue but accented with other colors.
- Need simple but smart looking pages after cover with lot of space; mostly we have text on the slides. Currently this is often in bullet point style, but we could probably upgrade the options there.
Should not have
- Anything that looks like a marketing style, as we typically use these with our current clients to share results of data collected, project plans, etc.

```html
<!DOCTYPE html>
<html lang="en">
<head>
<meta charset="utf-8">
<title>Report Cover — Kestrel</title>
<link rel="stylesheet" href="https://fonts.googleapis.com/css2?family=Source+Sans+3:wght@300;400;600&display=swap">
<style>
  :root {
    --paper: #ffffff;
    --ink-dark: #202020;
    --tab-dark: #232323;
    --brand-blue: #02394f;
    --text-light: #ffffff;
    --text-muted: #1e2326;
  }
  html, body {
    margin: 0;
    padding: 0;
    width: 793px;
    height: 1200px;
    overflow: hidden;
    background: var(--paper);
  }
  .page {
    position: relative;
    width: 793px;
    height: 1200px;
    overflow: hidden;
    font-family: "Source Sans 3", "Myriad Pro", Arial, sans-serif;
  }
  .shapes {
    position: absolute;
    inset: 0;
    width: 793px;
    height: 1200px;
  }
  .cover-field {
    position: absolute;
    left: 28px;
    margin: 0;
    font-weight: 400;
    font-size: 37px;
    line-height: 1;
    color: var(--text-light);
  }
  .cover-title { top: 180px; }
  .cover-date { top: 247px; }
  .confidential {
    position: absolute;
    left: 25px;
    top: 385px;
    margin: 0;
    font-size: 20px;
    font-weight: 300;
    line-height: 1;
    color: var(--text-muted);
  }
  .brand-tag {
    position: absolute;
    display: flex;
    align-items: center;
    gap: 8px;
    color: var(--text-light);
    font-weight: 600;
    font-size: 20px;
    letter-spacing: 2.5px;
    line-height: 1;
  }
  .brand-tag .brand-dot {
    width: 15px;
    height: 15px;
    border-radius: 50%;
    border: 2px solid var(--text-light);
    box-sizing: border-box;
  }
  .brand-tag--cover { left: 142px; top: 560px; }
  .brand-tag--footer { left: 160px; top: 1166px; font-size: 19px; }
</style>
</head>
<body>
<main class="page">
  <svg class="shapes" viewBox="0 0 760 1150" preserveAspectRatio="none" aria-hidden="true">
    <polygon class="wedge-dark" points="190,128 760,0 760,572 190,447" fill="var(--ink-dark)"/>
    <polygon class="wedge-blue" points="0,52 590,287 0,520" fill="var(--brand-blue)"/>
    <polygon class="tab-cover" points="10,572 188,502 506,572" fill="var(--tab-dark)"/>
    <polygon class="tab-footer" points="48,1150 200,1090 468,1150" fill="var(--tab-dark)"/>
  </svg>

  <h1 class="cover-field cover-title">Title :</h1>
  <p class="cover-field cover-date">Date:</p>
  <p class="confidential">CONFIDENTIAL</p>

  <div class="brand-tag brand-tag--cover"><span class="brand-dot"></span>KESTREL</div>
  <div class="brand-tag brand-tag--footer"><span class="brand-dot"></span>KESTREL</div>
</main>
</body>
</html>
```